Corvane: The Quiet Lantern

I need a front, back and spine cover for e and print for a short book. The book is called Corvane, subtitle, The Quiet Lantern. It is about an eyewitness to the Archangel Corvane. I would like to use the design many times with different colours for a series in spirituality and magic. So hopefully I can work with the designer again. The simple idea, is a plain cover in a colour, here blue. Mostly a font based cover, with a small symbolic image silhouetted at the bottom. Other covers will be orange, same font, and a different silhouette symbolic image and so on.

We need: a blue that will print well and look good on a screen. Serious, inviting honesty and truth and not flat. A font that is modern, female, says mystic but not old saint. The author is female and an award-winning writer in different areas. We need a uniform space for a title, (here Corvane), a uniform space for "The Quiet Lantern", a small space for a simple symbolic image, and author name, Wren Halloway. The small image on this blue cover should be in red. Ideas would be a simple rose head. The cover must look modern and professional and compliment the brand at www.wrenhalloway-books.com.

If the designer would simultaneously like to pitch to design the whole series (which will have many titles), another one would be a warm/hot pink background with the title Blue Harbour, subtitle, Brighten Every Ordinary Week. Small image silhouetted in orange might be a small gift shape, or a seahorse. Same author name, Wren Halloway. Another cover would be green background, title Lanterns: subtitle, Seven Rivers Beyond the Hill. Image in yellow: a rolled yoga mat, or an Om symbol. Wren Halloway. If we find a groove for the whole series, I can keep working with the same designer. Of course, the cover just for Corvane is fine here, but please bear in mind it fits into this wider series. Blue covers are about conversation with or contact with key spiritual figures, each from the author's own personal experience. Another one there would be "Swami Dhorelan", Letters From a Northern Garden. Image would be a simple daisy or a trophy emblem in red.

Font is crucial here and will define a series. Modern spirituality for the current generation. It must suggest contact with higher planes without being chintzy. Thank you!

Simple designs are iconic. That is what we are going for!

Good luck.

Target Market(s)

The people who read iconic series books like old marlow classics

Colors
34a6d7

Requirements
Must have
• modern, iconic, translatable into different markets.
Nice to have
• symbolic images silhouetted into a colour, not black, as the guidelines.
Should not have
• not too emotional.

```html
<!DOCTYPE html>
<html lang="en">
<head>
<meta charset="utf-8">
<title>Wren Halloway — Series Covers</title>
<link rel="stylesheet" href="https://fonts.googleapis.com/css2?family=Yellowtail&family=Lato:wght@300;400&display=swap">
<style>
  :root {
    --page-bg: #ffffff;
    --ink-light: #ffffff;
    --blue-top: #004fd9;
    --blue-bottom: #00a9ef;
    --pink-top: #e1005e;
    --pink-bottom: #f700c6;
    --green-top: #5fad24;
    --green-bottom: #cae565;
    --emblem-red: #d8202e;
    --emblem-violet: #7a28c8;
    --emblem-yellow: #f4ec14;
  }
  * { box-sizing: border-box; margin: 0; padding: 0; }
  html, body {
    width: 1200px;
    height: 840px;
    overflow: hidden;
    background: var(--page-bg);
  }
  .series {
    position: relative;
    width: 1200px;
    height: 840px;
  }
  .cover {
    position: absolute;
    top: 158px;
    width: 347px;
    height: 523px;
    color: var(--ink-light);
    text-align: center;
  }
  .cover--blue  { left: 41px;  background: linear-gradient(180deg, var(--blue-top), var(--blue-bottom)); }
  .cover--pink  { left: 427px; background: linear-gradient(180deg, var(--pink-top), var(--pink-bottom)); }
  .cover--green { left: 812px; background: linear-gradient(180deg, var(--green-top), var(--green-bottom)); }

  .cover__title {
    position: absolute;
    left: 0;
    right: 0;
    transform: translateY(-50%);
    font-family: "Yellowtail", cursive;
    font-weight: 400;
    font-size: 72px;
    line-height: 62px;
    transform-origin: center;
  }
  .cover__title--single { top: 152px; }
  .cover__title--stacked { top: 130px; }

  .cover__subtitle {
    position: absolute;
    left: 0;
    right: 0;
    transform: translateY(-50%);
    font-family: "Lato", sans-serif;
    font-weight: 300;
    font-size: 19px;
    line-height: 28px;
  }
  .cover--blue  .cover__subtitle { top: 202px; }
  .cover--pink  .cover__subtitle { top: 234px; }
  .cover--green .cover__subtitle { top: 220px; }

  .cover__emblem {
    position: absolute;
    left: 50%;
    top: 334px;
    width: 72px;
    height: 72px;
    transform: translate(-50%, -50%);
    border-radius: 50%;
  }
  .cover__emblem--rose     { background: var(--emblem-red); }
  .cover__emblem--seahorse { background: var(--emblem-violet); width: 44px; height: 104px; border-radius: 22px; }
  .cover__emblem--om       { background: var(--emblem-yellow); width: 90px; height: 90px; }

  .cover__author {
    position: absolute;
    left: 0;
    right: 0;
    top: 474px;
    transform: translateY(-50%);
    font-family: "Lato", sans-serif;
    font-weight: 400;
    font-size: 18px;
    letter-spacing: 0.06em;
    text-transform: uppercase;
  }
</style>
</head>
<body>
  <main class="series">
    <article class="cover cover--blue">
      <h1 class="cover__title cover__title--single">Corvane</h1>
      <p class="cover__subtitle">The Quiet Lantern</p>
      <div class="cover__emblem cover__emblem--rose" role="img" aria-label="Red silhouette of a rose head"></div>
      <p class="cover__author">Wren Halloway</p>
    </article>

    <article class="cover cover--pink">
      <h1 class="cover__title cover__title--stacked">Blue<br>Harbour</h1>
      <p class="cover__subtitle">Brighten Every Ordinary Week</p>
      <div class="cover__emblem cover__emblem--seahorse" role="img" aria-label="Violet silhouette of a seahorse"></div>
      <p class="cover__author">Wren Halloway</p>
    </article>

    <article class="cover cover--green">
      <h1 class="cover__title cover__title--single">Lanterns</h1>
      <p class="cover__subtitle">Seven Rivers<br>Beyond the Hill</p>
      <div class="cover__emblem cover__emblem--om" role="img" aria-label="Yellow lotus emblem with an Om symbol"></div>
      <p class="cover__author">Wren Halloway</p>
    </article>
  </main>
</body>
</html>
```